poster for a contemporary music concert series

Our association is hosting a series of contemporary music concerts.
The setup is classical - from chamber music trio, midsized ensemble until orchestra.
context/topic:
Every ensemble for contemporary music in the city is playing one concert in the series. We have one common topic each year. This year’s topic is about a composition idea  called "Tonverwebung". Each concert has one assigned student who is responsible to write a new piece that will be performed. This piece uses material generated by the LAST concert of the series. The used material can be anything (the score, the recording, a video recording, ...).
task:
We need a poster that will be printed in A3 format throughout the city before every concert. The poster must contain all the information of the concert series and must have places for the individual names of the performing ensemble/title/program.
The poster is used six times for six different ensembles. Although it is ONE series, we would like to have it easily visible that there are different concerts. We think the easiest way is to use complete different colors for background to distinguish the different ensembles/program titels from each other.
Things to be included on the poster:
- the title of the concert series is "de:turns".
- the concert place is "Lindenhof-Halle Dresden, großer Saal"
- the price is  "15€ normal / 10€ ermäßigt"
- the logo of TonGeflecht-Dresden can be used in any of the colours provided - somewhere should be mentioned, that this concert series is a cooperation "de:turns – Eine Konzertreihe von TonGeflecht-Dresden in Kooperation mit dem Lindenhof-Halle Dresden"
- the logo of the museum where we play is included and should be used
- the pdf shows examples of previous years
- there must be one bottom line in white for the needed logos of the funding partners. The funding partners are different from each concert, I included here three of them for visual purposes

Updates
- please don't use parts of the old posters. We have complete new posters for every year. The rectangle and the "Intelligenz" was part of last year's design.
- the music that is coming is not classical in a way that any instrument pictures would help to promote it. It's composed today, so very modern and often with use of electronics (de:turns is often inspired composers to a  kind of feedback, loop, variance, or ... of the previous material)

Target Market(s)
concert audience, young people
Industry/Entity Type
contemporary (classical) music
Requirements
Must have
- things mentioned in the brief description

Nice to have
- a visual look that shows that it is about contemporary music. IF there is any idea how to visualize the IDEA of the concert series this year (taking material from previous concerts and recompose it to the next ensemble) - this would be WONDERFUL. not necessary a copy, nor fake - just a reference to the old ones - and so on :-)

Should not have
- symbolic images/clipart/anything "musically" --> more avantgarde or abstract style is better

```html
<!DOCTYPE html>
<html lang="de">
<head>
<meta charset="utf-8">
<title>de:turns – Tonverwebung</title>
<link rel="stylesheet" href="https://fonts.googleapis.com/css2?family=Josefin+Sans:wght@600&family=Poiret+One&family=Ultra&family=Courier+Prime&family=Oranienbaum&family=Lexend:wght@400;500&family=Libre+Baskerville&display=swap">
<style>
  :root {
    --violet: #652382;
    --violet-deep: #3b1e78;
    --ink: #2a2a2a;
    --orange: #f39200;
    --white: #ffffff;
    --black: #111111;
    --venue-blue: #1ba0e2;
  }
  * { margin: 0; padding: 0; box-sizing: border-box; }
  html, body { width: 848px; height: 1200px; overflow: hidden; }
  body { background: var(--white); }
  .poster {
    position: relative;
    width: 848px; height: 1200px;
    background: var(--violet);
    overflow: hidden;
    font-family: "Lexend", sans-serif;
  }
  .artwork {
    position: absolute; left: 60px; top: 120px; width: 700px; height: 720px;
    background:
      radial-gradient(circle at 46% 30%, rgba(42,35,60,.55) 0 22%, transparent 40%),
      radial-gradient(circle at 82% 42%, rgba(42,35,60,.55) 0 16%, transparent 30%),
      radial-gradient(circle at 78% 72%, rgba(59,30,120,.7) 0 22%, transparent 38%),
      radial-gradient(circle at 34% 68%, rgba(59,30,120,.7) 0 16%, transparent 30%),
      radial-gradient(circle at 14% 86%, rgba(35,30,90,.7) 0 12%, transparent 24%);
  }
  .brand-host {
    position: absolute; left: 18px; top: 36px;
    display: flex; align-items: center; gap: 8px;
    color: var(--orange); font-size: 15px; font-weight: 500;
  }
  .brand-host .mark { width: 22px; height: 22px; background: var(--orange); }
  .brand-venue {
    position: absolute; right: 20px; top: 34px;
    display: flex; align-items: center; gap: 10px;
    color: var(--venue-blue); font-size: 17px; font-weight: 500; line-height: 1.05;
  }
  .brand-venue .mark { width: 48px; height: 48px; border-radius: 50%; background: var(--venue-blue); }
  .series-band {
    position: absolute; left: 0; top: 154px; width: 54px; height: 446px;
    background: var(--orange);
  }
  .series-band span {
    position: absolute; left: 50%; top: 50%;
    transform: translate(-50%, -50%) rotate(90deg);
    font-family: "Courier Prime", monospace; font-size: 50px; color: var(--black);
    white-space: nowrap; letter-spacing: -1px;
  }
  .title {
    position: absolute; left: 70px; top: 146px;
    font-family: "Josefin Sans", sans-serif; font-weight: 600;
    color: var(--white); font-size: 128px; line-height: 116px;
    letter-spacing: 4px;
  }
  .title span { display: block; }
  .program {
    position: absolute; right: 160px; top: 556px; text-align: right;
    font-family: "Poiret One", sans-serif; color: var(--white);
    font-size: 36px; line-height: 43.6px;
  }
  .date-box {
    position: absolute; left: 344px; top: 855px; width: 504px; height: 87px;
    background: var(--orange); padding: 12px 0 0 21px;
    font-family: "Ultra", serif; color: var(--black);
  }
  .date-box .when { font-size: 28px; line-height: 34px; }
  .date-box .time { color: var(--white); }
  .date-box .where { font-size: 18px; line-height: 30px; margin-top: 4px; }
  .cooperation {
    position: absolute; left: 347px; top: 958px; width: 480px;
    font-family: "Oranienbaum", serif; color: var(--white);
    font-size: 17px; line-height: 22px;
  }
  .cooperation b { font-family: "Courier Prime", monospace; color: var(--orange); font-weight: 700; }
  .tickets {
    position: absolute; right: 18px; top: 1072px;
    font-family: "Courier Prime", monospace; color: var(--white); font-size: 21px;
  }
  .funding-bar {
    position: absolute; left: 0; top: 1108px; width: 848px; height: 92px;
    background: var(--white);
  }
  .access-note {
    position: absolute; left: 47px; top: 42px;
    font-size: 11px; font-weight: 500; line-height: 15px; color: var(--black);
  }
  .funder-city {
    position: absolute; left: 440px; top: 26px; display: flex; align-items: flex-start; gap: 10px;
  }
  .funder-city .label { font-size: 7.5px; line-height: 9px; color: #444; text-align: right; width: 100px; }
  .funder-city .crest { width: 24px; height: 28px; background: var(--black); }
  .funder-city .rule { width: 1px; height: 46px; background: #555; }
  .funder-city .name { font-family: "Libre Baskerville", serif; font-size: 16px; color: var(--black); }
  .funder-state { position: absolute; left: 726px; top: 22px; width: 84px; }
  .funder-state .badges { display: flex; justify-content: space-between; }
  .funder-state .badge-a { width: 50px; height: 36px; background: #9cc35a; }
  .funder-state .badge-b { width: 22px; height: 34px; background: #2e8b3a; }
  .funder-state .fine { font-family: "Libre Baskerville", serif; font-size: 3px; line-height: 3.6px; margin-top: 4px; color: #333; }
</style>
</head>
<body>
<div class="poster">
  <div class="artwork" role="img" aria-label="Abstrakte, dunkle Pinselkreise und Farbspritzer in Violett und Blau"></div>

  <div class="brand-host"><span class="mark"></span>TonGeflecht Dresden</div>
  <div class="brand-venue"><span class="mark"></span>Lindenhof-Halle<br>Dresden</div>

  <div class="series-band"><span>de:turns</span></div>

  <h1 class="title"><span>TON</span><span>VER</span><span>WE</span><span>BUNG</span></h1>

  <div class="program">
    WERKE VON<br>JORIS VAN AELST<br>PIETER DE LA HAYE<br>TIM JANSEN<br>PAVEL BRZÁK<br>GUSTAVO ALMEIDA
  </div>

  <div class="date-box">
    <div class="when">Fr. 10. Jun 2022 <span class="time">19:30 Uhr</span></div>
    <div class="where">Lindenhof-Halle Dresden, großer Saal</div>
  </div>

  <p class="cooperation"><b>de:turns</b> – Eine Konzertreihe von TonGeflecht-Dresden in Kooperation mit dem Lindenhof-Halle Dresden</p>

  <p class="tickets">Tickets: 15€ normal / 10€ ermäßigt</p>

  <footer class="funding-bar">
    <p class="access-note">Zutritt für alle Besucher*innen ausschließlich mit einem negativen<br>Corona-Test nicht älter als 24 h, Impf- oder Genesenen-Nachweis.</p>
    <div class="funder-city">
      <p class="label">gefördert durch<br>das Amt für Stadtkultur<br>und Baupflege</p>
      <span class="crest"></span>
      <span class="rule"></span>
      <span class="name">Elbstadt.</span>
    </div>
    <div class="funder-state">
      <div class="badges"><span class="badge-a"></span><span class="badge-b"></span></div>
      <p class="fine">Gefördert durch den Landesfonds Kunst. Diese Maßnahme wird mitfinanziert durch Steuermittel auf Grundlage des beschlossenen Haushaltes.</p>
    </div>
  </footer>
</div>
</body>
</html>
```